依頼詳細
運動の嫌いな子でも気軽に身体を動かせるような教室を目指しています。
現在は低学年の女子が主な受講生なので、男子や高学年の子ども達にも興味を持っていただけたらありがたいです。
配布方法は新聞への折り込みなどを考えています。
白黒で印刷してもキレイに見えるデザインを希望します。
記載項目
現在使っているチラシ(wordファイル)を添付しています。
記載項目はその内容でお願いいたします。
サイズ
A4
ページ数
片面
希望イメージ
シンプル 複雑
単色 カラフル
暗い 明るい
日常 高級
遊び心 厳粛
未来的 伝統的
女性的 男性的
希望する色
納品ファイル
• 高解像度JPG (.jpg)
補足説明
■ 選んだ理由

ぱっと目を引く明るいデザインと、雰囲気が当教室とマッチしていることから決定いたしました。
PRポインとや、目線の流れもわかりやすく、白黒バージョンも見やすかったです。

■ 提案者全員のお礼・コメント

ご提案いただいた皆様
この度は沢山のご提案をいただき、まことにありがとうございました。
初めてのポルテミカの利用でしたが、素晴らしいご提案をたくさんいただけたことに感激しました。
ぜひこれからも依頼させていただきたいと思います。
よろしくお願いいたします。

```html
<!DOCTYPE html>
<html lang="ja">
<head>
<meta charset="utf-8">
<title>はるかぜキッズダンス 森山教室のご案内</title>
<link rel="stylesheet" href="https://fonts.googleapis.com/css2?family=M+PLUS+Rounded+1c:wght@500;700;800;900&display=swap">
<style>
:root{
  --green:#3aa336;
  --green-dark:#1f7d2a;
  --yellow:#ffe04a;
  --orange:#f08a1c;
  --brown:#6b3a12;
  --pink:#e8438a;
  --blue:#1f8fd6;
  --text:#333;
  --white:#fff;
}
*{box-sizing:border-box;margin:0;padding:0}
html,body{width:849px;height:1200px;overflow:hidden;background:#fff}
body{font-family:"M PLUS Rounded 1c",sans-serif;color:var(--text)}
.flyer{position:relative;width:849px;height:1200px;overflow:hidden;
  background:radial-gradient(ellipse at 30% 25%,#fffbe0 0,#fff3a0 40%,#ffe96a 80%) top/100% 670px no-repeat,#fff}
.badges{position:absolute;left:22px;top:14px;display:flex;gap:8px}
.badge{width:90px;height:90px;border-radius:50%;color:#fff;font-weight:900;font-size:18px;line-height:1.05;
  display:flex;align-items:center;justify-content:center;text-align:center;border:4px solid #fff;box-shadow:0 2px 0 rgba(0,0,0,.12)}
.badge--green{background:var(--green)}
.badge--pink{background:var(--pink);font-size:16px}
.badge--blue{background:var(--blue)}
.hero-kids{position:absolute;left:430px;top:8px;width:400px;height:250px;border-radius:30px;
  background:linear-gradient(135deg,#ffd27a,#9fd86a)}
.title{position:absolute;left:70px;top:118px;font-weight:900}
.title__main{display:block;font-size:84px;color:var(--green);line-height:1.02;
  -webkit-text-stroke:12px #fff;paint-order:stroke fill;text-shadow:4px 5px 0 rgba(0,0,0,.18)}
.title__sub{display:block;font-size:50px;color:var(--brown);margin-top:4px;
  -webkit-text-stroke:8px #fff;paint-order:stroke fill}
.fee{position:absolute;left:22px;top:356px;width:150px;height:120px;border-radius:50%;background:var(--orange);
  color:#fff;text-align:center;font-weight:900;border:4px solid #fff;display:flex;flex-direction:column;justify-content:center}
.fee__label{font-size:19px}
.fee__price{font-size:20px;line-height:1.05}
.fee__price b{font-size:38px}
.intro{position:absolute;left:200px;top:364px;width:625px;font-size:14px;font-weight:700;line-height:1.55;color:var(--brown)}
.intro__note{color:var(--pink)}
.class-photo{position:absolute;left:334px;top:414px;width:492px;height:142px;border-radius:10px;
  background:linear-gradient(90deg,#6d8fa8,#c9b08a);border:4px solid #fff}
.music{position:absolute;left:40px;top:522px;width:290px;color:var(--brown);font-weight:900}
.music__list{font-size:22px;line-height:1.3}
.music__more{font-size:16px;margin-top:2px}
.points{position:absolute;left:462px;top:568px;width:370px;list-style:none;font-size:15px;font-weight:700;line-height:1.45;color:var(--brown)}
.points li{position:relative;padding-left:28px;margin-bottom:8px}
.points svg{position:absolute;left:0;top:2px}
.details{position:absolute;left:28px;top:682px;width:504px;border-collapse:collapse}
.details th{width:76px;background:var(--orange);color:#fff;font-size:17px;font-weight:900;padding:6px 0;
  text-align:center;border-bottom:3px solid #fff;vertical-align:middle}
.details td{padding:6px 12px;font-size:14px;font-weight:700;line-height:1.4;border-bottom:2px dotted #f0b060}
.details .big{font-size:28px;font-weight:900;color:var(--green-dark)}
.details .big span{font-size:22px}
.details .outfit{display:flex;align-items:center;gap:10px}
.outfit__art{width:100px;height:56px;border-radius:8px;background:linear-gradient(135deg,#9ee07a,#f4f4f4);flex:none}
.teacher{position:absolute;left:550px;top:682px;width:276px;height:266px;border:3px solid var(--orange);border-radius:14px;background:#fff}
.teacher__tag{position:absolute;left:10px;top:10px;width:60px;height:60px;border-radius:50%;background:var(--orange);color:#fff;
  font-weight:900;font-size:15px;line-height:1.1;display:flex;align-items:center;justify-content:center;text-align:center}
.teacher__photo{position:absolute;right:14px;top:12px;width:180px;height:140px;border-radius:8px;background:linear-gradient(180deg,#d8e6ef,#9c7a5c)}
.teacher__name{position:absolute;left:14px;top:162px;font-size:22px;font-weight:900;color:var(--brown)}
.teacher__bio{position:absolute;right:14px;top:198px;font-size:11.5px;font-weight:700;line-height:1.4;text-align:right}
.notes{position:absolute;left:28px;top:966px;width:798px;height:88px;border:3px solid var(--green);border-radius:12px;padding:16px 16px 6px}
.notes__tag{position:absolute;left:14px;top:-13px;background:var(--green);color:#fff;font-size:13px;font-weight:900;padding:2px 14px;border-radius:14px}
.notes ul{list-style:none;font-size:12px;line-height:1.6;font-weight:500}
.notes li::before{content:"・"}
.contact{position:absolute;left:0;top:1064px;width:849px;height:136px;background:var(--green);color:#fff;padding:26px 28px}
.contact__name{font-size:22px;font-weight:900}
.contact__call{font-size:24px;font-weight:900;margin-top:12px;color:var(--yellow)}
.contact__phones{position:absolute;right:24px;top:16px;text-align:right}
.phone{display:flex;align-items:center;justify-content:flex-end;gap:8px;font-size:34px;font-weight:900;line-height:1.45}
.phone small{font-size:14px}
</style>
</head>
<body>
<main class="flyer">
  <div class="badges">
    <div class="badge badge--green">体力<br>UP!</div>
    <div class="badge badge--pink">リズム感<br>UP!</div>
    <div class="badge badge--blue">調整力<br>UP!</div>
  </div>
  <div class="hero-kids" role="img" aria-label="元気に踊る男の子と女の子のイラスト"></div>

  <h1 class="title">
    <span class="title__main">はるかぜ<br>キッズダンス</span>
    <span class="title__sub">森山教室のご案内</span>
  </h1>

  <div class="fee">
    <div class="fee__label">レッスン料</div>
    <div class="fee__price">1回<b>500</b>円</div>
  </div>

  <p class="intro">入会手続きなどはありません。月に1回でも、お気軽にご参加ください。<br><span class="intro__note">お支払いは1回ごとです。他の方法をご希望の方はご相談ください。</span></p>

  <div class="class-photo" role="img" aria-label="教室でダンスを練習する子どもたちの写真"></div>

  <div class="music">
    <div class="music__list">ヒーローソング、<br>アニメソング、魔法少女ソング、<br>人気ダンス曲</div>
    <div class="music__more">その他ダンスミュージック<br>(リクエスト歓迎!)</div>
  </div>

  <ul class="points">
    <li><svg width="20" height="20" viewBox="0 0 22 22"><circle cx="11" cy="11" r="11" fill="#f08a1c"/><path d="M6 11l4 4 7-8" stroke="#fff" stroke-width="3" fill="none" stroke-linecap="round"/></svg>楽しく踊りながら、体力の向上と<br>リズム感・調整力を養います。</li>
    <li><svg width="20" height="20" viewBox="0 0 22 22"><circle cx="11" cy="11" r="11" fill="#f08a1c"/><path d="M6 11l4 4 7-8" stroke="#fff" stroke-width="3" fill="none" stroke-linecap="round"/></svg>体力に自信のない子や男子でも、<br>気軽に参加できる教室を目指しています。</li>
  </ul>

  <table class="details">
    <tr><th>日 時</th><td class="big">毎週水曜日 <span>17:00〜18:00</span></td></tr>
    <tr><th>場 所</th><td>森山町ひだまりセンター2階 研修室</td></tr>
    <tr><th>対 象</th><td>小学生(保育園児は保護者の同伴をお願いします)<br>保護者のレッスン参加は無料です</td></tr>
    <tr><th>服 装</th><td class="outfit"><span>動きやすい服・靴<br>汗をかきますので、<br>着替えがあると安心です</span><span class="outfit__art" role="img" aria-label="運動着と運動靴のイラスト"></span></td></tr>
    <tr><th>持ち物</th><td>飲み物、タオル</td></tr>
  </table>

  <section class="teacher">
    <div class="teacher__tag">講師<br>紹介</div>
    <div class="teacher__photo" role="img" aria-label="講師の写真"></div>
    <div class="teacher__name">川村 真由美</div>
    <div class="teacher__bio">東原町在住(はるかぜ体操クラブ)<br>元エアロビクスインストラクター<br>ロックダンサー</div>
  </section>

  <section class="notes">
    <div class="notes__tag">保護者の方へ</div>
    <ul>
      <li>会場では上靴をご用意ください。更衣室はありませんので、着替えはお家でお願いします。</li>
      <li>レッスン中の様子を撮影する場合があります。掲載を希望されない方はお知らせください。</li>
      <li>お休みの連絡は不要です。体調のすぐれない日は無理せずお休みください。</li>
    </ul>
  </section>

  <footer class="contact">
    <div class="contact__name">はるかぜキッズダンス(森山教室)</div>
    <div class="contact__call">お気軽にお問い合わせ下さい!</div>
    <div class="contact__phones">
      <div class="phone"><svg width="28" height="28" viewBox="0 0 24 24"><path fill="#fff" d="M6.6 10.8a15 15 0 006.6 6.6l2.2-2.2c.3-.3.7-.4 1-.2 1.1.4 2.3.6 3.6.6.6 0 1 .4 1 1V20c0 .6-.4 1-1 1A17 17 0 013 4c0-.6.4-1 1-1h3.5c.6 0 1 .4 1 1 0 1.3.2 2.5.6 3.6.1.3 0 .7-.2 1z"/></svg>080-4172-3058<small>(沢口 健)</small></div>
      <div class="phone"><svg width="28" height="28" viewBox="0 0 24 24"><path fill="#fff" d="M6.6 10.8a15 15 0 006.6 6.6l2.2-2.2c.3-.3.7-.4 1-.2 1.1.4 2.3.6 3.6.6.6 0 1 .4 1 1V20c0 .6-.4 1-1 1A17 17 0 013 4c0-.6.4-1 1-1h3.5c.6 0 1 .4 1 1 0 1.3.2 2.5.6 3.6.1.3 0 .7-.2 1z"/></svg>080-2946-5810<small>(沢口 さやか)</small></div>
    </div>
  </footer>
</main>
</body>
</html>
```